Kestrel Ledger Stationary
Business cards and MS Word letterhead template
Creative Brief
Use same font as used in my logo
Bank Gothic
Modern
Marcus Bellweather
Chief Operating Officer
4826 N Halvern RD, STE 212 Tempe, AZ 85291
marcus.bellweather@kestrelledger.example
www.kestrelledger.example
Stationary requirements: MS Word template with logo, address and phone in the header. Vector graphics Color and grayscale
Logo or other design element and the following text: "Kestrel Ledger, LLC is a registered ISO/MSP of Harwick Savings and Loan."

```html
<!DOCTYPE html>
<html lang="en">
<head>
<meta charset="utf-8">
<title>Kestrel Ledger Stationery</title>
<link href="https://fonts.googleapis.com/css2?family=Michroma&family=Open+Sans:wght@400;600&display=swap" rel="stylesheet">
<style>
  :root {
    --blue: #3d63b3;
    --blue-faint: #e6ecf6;
    --grey: #7b7e84;
    --grey-light: #c9ccd1;
    --paper: #ffffff;
    --ink: #3a3d44;
    --backdrop: #e9e5de;
    --label: #5b5144;
  }
  * { margin: 0; padding: 0; box-sizing: border-box; }
  html, body { width: 1200px; height: 446px; overflow: hidden; }
  body {
    background: var(--backdrop);
    font-family: "Open Sans", Arial, sans-serif;
    color: var(--ink);
    position: relative;
  }
  .piece { position: absolute; background: var(--paper); box-shadow: 0 1px 4px rgba(0,0,0,.18); overflow: hidden; }
  .piece svg.corners { position: absolute; inset: 0; width: 100%; height: 100%; }
  .label {
    position: absolute; font-family: "Michroma", sans-serif; font-size: 5.5px;
    letter-spacing: .6px; color: var(--label); text-transform: uppercase;
  }
  .brand { display: flex; align-items: center; gap: 4px; position: absolute; }
  .brand-square { background: var(--blue); border-radius: 2px; }
  .brand-name { font-family: "Michroma", sans-serif; color: var(--blue); text-transform: uppercase; line-height: 1; }
  .watermark { position: absolute; background: var(--blue-faint); border-radius: 14%; }
  .small-text { position: absolute; font-size: 3.6px; line-height: 1.5; color: var(--grey); }

  /* business cards */
  .card { left: 19px; width: 106px; height: 72px; }
  .card-front { top: 226px; }
  .card-back { top: 332px; }
  .card .brand { left: 8px; top: 10px; }
  .card .brand-square { width: 12px; height: 12px; }
  .card .brand-name { font-size: 6.5px; }

  /* letterheads */
  .letterhead { top: 10px; width: 305px; height: 398px; }
  .letterhead-one { left: 163px; }
  .letterhead-two { left: 486px; }
  .letterhead .brand { left: 18px; top: 18px; }
  .letterhead .brand-square { width: 16px; height: 16px; }
  .letterhead .brand-name { font-size: 9px; }

  /* envelopes */
  .envelope-back { left: 816px; width: 372px; height: 96px; }
  .envelope-blue { top: 12px; background: var(--blue); }
  .envelope-grey { top: 86px; background: var(--grey); }
  .envelope-white { top: 160px; height: 66px; }
  .envelope-back svg { position: absolute; inset: 0; width: 100%; height: 100%; }
  .seal { position: absolute; left: 176px; width: 20px; height: 20px; border-radius: 3px; }
  .envelope-front { left: 816px; top: 236px; width: 372px; height: 172px; }
  .envelope-front .brand { left: 16px; top: 14px; }
  .envelope-front .brand-square { width: 13px; height: 13px; }
  .envelope-front .brand-name { font-size: 7px; }
</style>
</head>
<body>

<div class="label" style="left:20px;top:172px;">Stationery Concepts</div>

<!-- Business card front -->
<div class="piece card card-front">
  <svg class="corners" viewBox="0 0 106 72" preserveAspectRatio="none">
    <path d="M70 72 Q96 66 106 40 L106 72 Z" fill="var(--blue)"/>
    <path d="M62 72 Q94 66 106 34" fill="none" stroke="var(--grey-light)" stroke-width=".8"/>
  </svg>
  <div class="brand"><span class="brand-square"></span><span class="brand-name">Kestrel<br>Ledger</span></div>
  <div class="small-text" style="left:8px;top:34px;font-weight:600;color:var(--ink);font-size:4.4px;">Marcus Bellweather</div>
  <div class="small-text" style="left:8px;top:41px;">Chief Operating Officer</div>
</div>
<div class="label" style="left:20px;top:304px;">Business Card Front</div>

<!-- Business card back -->
<div class="piece card card-back">
  <svg class="corners" viewBox="0 0 106 72" preserveAspectRatio="none">
    <path d="M0 0 L40 0 Q12 5 0 30 Z" fill="var(--blue)"/>
  </svg>
  <div class="brand" style="top:8px;left:24px;"><span class="brand-square"></span><span class="brand-name">Kestrel<br>Ledger</span></div>
  <div class="small-text" style="left:24px;top:30px;">4826 N Halvern RD, STE 212<br>Tempe, AZ 85291<br>marcus.bellweather@kestrelledger.example<br>www.kestrelledger.example</div>
</div>
<div class="label" style="left:20px;top:410px;">Business Card Back</div>

<!-- Letterhead option 1 -->
<div class="piece letterhead letterhead-one">
  <svg class="corners" viewBox="0 0 305 398" preserveAspectRatio="none">
    <path d="M262 0 L305 0 L305 40 Q296 10 262 0 Z" fill="var(--blue)"/>
    <path d="M250 0 Q298 8 305 50" fill="none" stroke="var(--grey-light)" stroke-width="1"/>
    <path d="M0 348 Q8 388 48 398 L0 398 Z" fill="var(--blue)"/>
    <path d="M0 338 Q6 392 58 398" fill="none" stroke="var(--grey-light)" stroke-width="1"/>
  </svg>
  <div class="brand"><span class="brand-square"></span><span class="brand-name">Kestrel<br>Ledger</span></div>
  <div class="small-text" style="right:40px;top:16px;text-align:right;">4826 N Halvern RD, STE 212<br>Tempe, AZ 85291<br>Phone: (480) 555-0148<br>www.kestrelledger.example</div>
  <div class="watermark" style="left:184px;top:266px;width:84px;height:84px;"></div>
</div>
<div class="label" style="left:270px;top:418px;">Letterhead Option 1</div>

<!-- Letterhead option 2 -->
<div class="piece letterhead letterhead-two">
  <svg class="corners" viewBox="0 0 305 398" preserveAspectRatio="none">
    <path d="M262 0 L305 0 L305 40 Q296 10 262 0 Z" fill="var(--blue)"/>
    <path d="M250 0 Q298 8 305 50" fill="none" stroke="var(--grey-light)" stroke-width="1"/>
    <path d="M0 348 Q8 388 48 398 L0 398 Z" fill="var(--blue)"/>
    <path d="M0 338 Q6 392 58 398" fill="none" stroke="var(--grey-light)" stroke-width="1"/>
  </svg>
  <div class="brand" style="left:102px;"><span class="brand-square"></span><span class="brand-name">Kestrel<br>Ledger</span></div>
  <div class="watermark" style="left:110px;top:142px;width:86px;height:86px;"></div>
  <div class="small-text" style="left:0;right:0;top:378px;text-align:center;">Kestrel Ledger, LLC is a registered ISO/MSP of Harwick Savings and Loan. · 4826 N Halvern RD, STE 212 Tempe, AZ 85291</div>
</div>
<div class="label" style="left:596px;top:418px;">Letterhead Option 2</div>

<!-- Envelope backs -->
<div class="piece envelope-back envelope-blue">
  <svg viewBox="0 0 372 96" preserveAspectRatio="none"><path d="M0 0 L186 58 L372 0" fill="none" stroke="rgba(255,255,255,.35)" stroke-width="1"/></svg>
  <span class="seal" style="top:40px;background:var(--paper);"></span>
</div>
<div class="piece envelope-back envelope-grey">
  <svg viewBox="0 0 372 96" preserveAspectRatio="none">
    <path d="M0 0 L372 0 L372 18 Q186 62 0 18 Z" fill="#5f6268"/>
  </svg>
  <span class="seal" style="top:34px;background:var(--paper);"></span>
</div>
<div class="piece envelope-back envelope-white">
  <svg viewBox="0 0 372 66" preserveAspectRatio="none">
    <path d="M0 10 Q186 52 372 10" fill="none" stroke="var(--grey-light)" stroke-width="1"/>
  </svg>
  <span class="seal" style="top:26px;background:var(--blue);"></span>
</div>

<!-- Envelope front -->
<div class="piece envelope-front">
  <svg class="corners" viewBox="0 0 372 172" preserveAspectRatio="none">
    <path d="M336 0 L372 0 L372 30 Q366 6 336 0 Z" fill="var(--blue)"/>
    <path d="M326 0 Q368 6 372 40" fill="none" stroke="var(--grey-light)" stroke-width="1"/>
  </svg>
  <div class="brand"><span class="brand-square"></span><span class="brand-name">Kestrel<br>Ledger</span></div>
  <div class="small-text" style="left:16px;top:34px;">4826 N Halvern RD, STE 212<br>Tempe, AZ 85291</div>
  <div class="watermark" style="left:292px;top:96px;width:66px;height:66px;"></div>
</div>
<div class="label" style="left:962px;top:418px;">Envelope Option 1</div>

</body>
</html>
```